Brivolan - presentation for a remote DBA team offering data platform management

We need a website design for wordpress site called Brivolan.cz
We deliver remote database and data platform administration and development, oversee the database administrators, consult and train the personnel responsible for the database operations. The website should include several sections, home page with graphics elements supporting the name and service - remote dba work; blog section; service introduction and description, team introduction and description, download section for documents, presentations etc.

Target Market(s)

small and medium business companies requiring remote DBA service

Number of Pages Required

3 page

Font styles to use
Sans Serif

Colors

Designer to choose colors to be used in the design.

Requirements
Must have
• The website should have several sections to introduce the services, blog, team introduction, downloads

```html
<!DOCTYPE html>
<html lang="en">
<head>
<meta charset="utf-8">
<title>Brivolan – Remote DBA Team</title>
<link rel="stylesheet" href="https://fonts.googleapis.com/css2?family=Poppins:wght@400;500;600;700;800&family=Montserrat:wght@400;500;600&display=swap">
<style>
:root{
  --purple:#5a2fd6;
  --purple-deep:#4a22b8;
  --violet:#7a3cf0;
  --blue:#2a6ee0;
  --blue-title:#2d6fdc;
  --ink:#2b2b3a;
  --text:#555566;
  --white:#ffffff;
  --footer-bg:#f1f1f4;
  --line:#d8d8e0;
}
*{box-sizing:border-box;margin:0;padding:0}
html,body{width:1200px;height:3607px;overflow:hidden;background:var(--white)}
body{position:relative;font-family:"Montserrat",sans-serif;color:var(--text)}
.abs{position:absolute}
.heading{font-family:"Poppins",sans-serif;font-weight:700}

/* top bar */
.topbar{top:0;left:0;width:1200px;height:53px;border-bottom:1px solid #e4e4ea;font-size:13px;color:#444}
.topbar .phone{left:120px;top:18px}
.topbar .right{right:120px;top:17px;display:flex;gap:9px;align-items:center}
.dot{width:10px;height:10px;border-radius:50%;background:#444;display:inline-block}

/* nav */
.nav{top:53px;left:0;width:1200px;height:79px}
.logo{font-family:"Poppins",sans-serif;font-weight:800;color:var(--purple);letter-spacing:1px}
.nav .logo{left:120px;top:20px;font-size:34px}
.nav ul{list-style:none;position:absolute;top:28px;left:0;width:1200px}
.nav li{position:absolute;font-family:"Poppins",sans-serif;font-size:16px;font-weight:500;color:#444}
.nav li.active{color:var(--purple)}

/* hero */
.hero{top:132px;left:0;width:1200px;height:580px;background:linear-gradient(180deg,#2a3340 0%,#1b2230 60%,#101622 100%)}
.hero-title{top:240px;width:1200px;text-align:center;color:#fff;font-size:34px}
.hero-sub{top:295px;width:1200px;text-align:center;color:#fff;font-size:26px;line-height:38px;font-family:"Montserrat",sans-serif}
.follow{left:56px;top:155px;display:flex;flex-direction:column;gap:30px;align-items:center}
.follow .dot{background:#fff;width:12px;height:12px}
.follow-label{left:32px;top:390px;transform:rotate(-90deg);color:#fff;font-size:13px}
.slides{left:1120px;top:245px;display:flex;flex-direction:column;gap:22px}
.slides span{width:8px;height:8px;border-radius:50%;background:var(--blue)}
.slide-num{left:1080px;top:240px;color:#fff;font-size:12px}

/* about */
.about-img{left:89px;top:777px;width:496px;height:442px;background:linear-gradient(135deg,#1a1f3a,#2b3c7a 55%,#141a30)}
.about-card{left:519px;top:818px;width:578px;height:360px;background:#fff;box-shadow:0 6px 24px rgba(0,0,0,.12);padding:55px 41px}
.section-title{font-family:"Poppins",sans-serif;font-weight:700;color:var(--blue-title)}
.about-card h2{font-size:34px}
.about-card p{margin-top:18px;font-size:15px;line-height:30px;color:#444}
.btn{display:inline-block;background:var(--purple);color:#fff;font-family:"Poppins",sans-serif;font-weight:600;border-radius:24px;text-align:center}
.about-card .btn{margin-top:20px;width:133px;height:41px;line-height:41px;font-size:15px}

/* dba band */
.dba{top:1284px;left:0;width:1200px;height:411px;background:linear-gradient(90deg,#f3f5fa 0%,#eef1f7 45%,#c7d3e6 62%,#3a5a86 100%)}
.dba h2{left:99px;top:40px;font-size:26px;line-height:48px;color:var(--blue-title)}
.dba p{left:99px;top:148px;width:620px;font-size:14.5px;line-height:29px;color:#444}
.dba .btn{left:99px;top:315px;width:149px;height:46px;line-height:46px;font-size:15px}

/* services */
.services-title{top:1745px;width:1200px;text-align:center;font-size:34px}
.services-text{top:1808px;width:1200px;text-align:center;font-size:17px;line-height:29px;color:#444}
.card{top:1912px;width:340px;height:267px}
.card-photo{background:linear-gradient(135deg,#cfc8c2,#8f8a86)}
.card-feature{background:var(--violet);color:#fff;display:flex;align-items:center;justify-content:center;text-align:center;font-family:"Poppins",sans-serif;font-weight:600;font-size:18px;line-height:34px}
.card-photo.tech{background:linear-gradient(135deg,#2c3a55,#5a6b88)}
.card-arrow{right:8px;bottom:8px;width:40px;height:36px;background:#222}

/* testimonials */
.testi{top:2239px;left:0;width:1200px;height:505px;background:linear-gradient(180deg,#7433ea 0%,#5d28c8 100%)}
.testi h2{top:48px;width:1200px;text-align:center;color:#fff;font-size:34px}
.testi blockquote{top:130px;left:320px;width:560px;text-align:center;color:#fff;font-size:14px;line-height:30px}
.testi .name{top:236px;width:1200px;text-align:center;color:#fff;font-family:"Poppins",sans-serif;font-size:20px;font-weight:500;letter-spacing:1px}
.avatar{border-radius:50%;background:linear-gradient(180deg,#9aa0c0,#5b5f86);border:3px solid rgba(255,255,255,.5)}
.avatar.main{border:5px solid #fff;background:linear-gradient(180deg,#c9b6a6,#6b5a50)}
.track{left:197px;top:445px;width:806px;height:2px;background:rgba(255,255,255,.35)}
.track span{position:absolute;left:359px;top:-2px;width:86px;height:5px;background:#fff}

/* contact */
.contact{top:2744px;left:0;width:1200px;height:515px;background:linear-gradient(180deg,#2f7ae6,#2160cf)}
.contact h2{top:78px;width:1200px;text-align:center;color:#fff;font-size:34px}
.field{background:#fff;height:39px;font-size:11px;color:#666;padding:12px 14px}
.contact .btn{left:539px;top:394px;width:120px;height:41px;line-height:41px;font-size:16px}

/* footer */
.footer{top:3259px;left:0;width:1200px;height:272px;background:var(--footer-bg)}
.footer .logo{left:106px;top:68px;font-size:46px}
.footer .tag{left:106px;top:144px;font-size:13px;line-height:24px;color:#333}
.subscribe{left:103px;top:197px;width:241px;height:38px;border:1px solid #ccc;background:#fff;font-size:11px;font-style:italic;color:#777;padding:12px}
.subscribe span{position:absolute;right:0;top:-1px;width:44px;height:38px;background:var(--purple-deep)}
.fcol h3{font-family:"Poppins",sans-serif;font-weight:700;font-size:18px;color:var(--purple)}
.fcol ul{list-style:none;margin-top:20px}
.links li{font-size:12.5px;color:#333;line-height:23.5px;padding-left:16px;position:relative}
.links li::before{content:"";position:absolute;left:2px;top:8px;border-left:5px solid #333;border-top:4px solid transparent;border-bottom:4px solid transparent}
.info li{font-size:13px;color:#333;line-height:20px;padding-left:34px;position:relative;margin-bottom:12px}
.info li svg{position:absolute;left:0;top:2px}
.social li{font-size:13.5px;color:var(--purple-deep);line-height:22px;padding-left:32px;position:relative;margin-bottom:14px}
.social li::before{content:"";position:absolute;left:0;top:0;width:20px;height:20px;border:2px solid var(--purple-deep);border-radius:50%}
.bottom{top:3531px;left:0;width:1200px;height:76px;border-top:1px solid var(--line);text-align:center;font-size:13px;color:#333;line-height:74px}
</style>
</head>
<body>

<header class="abs topbar">
  <div class="abs phone">&#9742; 555 - (555) 0142</div>
  <div class="abs right"><span class="dot"></span><span class="dot"></span><span class="dot"></span><span class="dot"></span><span style="color:#999">|</span><span>Login &#10140;</span></div>
</header>

<nav class="abs nav">
  <div class="abs logo">BRIVOLAN</div>
  <ul>
    <li class="active" style="left:543px">Home</li>
    <li style="left:622px">About us</li>
    <li style="left:725px">Services</li>
    <li style="left:825px">Our Team</li>
    <li style="left:937px">Blog</li>
    <li style="left:1002px">Contact</li>
  </ul>
</nav>

<section class="abs hero" role="img" aria-label="Two engineers reviewing a laptop in a server room">
  <div class="abs follow"><span class="dot"></span><span class="dot"></span><span class="dot"></span><span class="dot"></span></div>
  <div class="abs follow-label">Follow us</div>
  <div class="abs heading hero-title">DATA PLATFORM MANAGEMENT</div>
  <div class="abs hero-sub">Lorem ipsum dolor sit amet, consectetur<br>adipiscing elit</div>
  <div class="abs slide-num">01</div>
  <div class="abs slides"><span></span><span></span><span></span><span></span></div>
  <svg class="abs" style="left:0;top:546px" width="1200" height="34" viewBox="0 0 1200 34" preserveAspectRatio="none">
    <path d="M0 18 q15 -9 30 0 q15 9 30 0 q15 -9 30 0 q15 9 30 0 q15 -9 30 0 q15 9 30 0 q15 -9 30 0 q15 9 30 0 q15 -9 30 0 q15 9 30 0 q15 -9 30 0 q15 9 30 0 q15 -9 30 0 q15 9 30 0 q15 -9 30 0 q15 9 30 0 q15 -9 30 0 q15 9 30 0 q15 -9 30 0 q15 9 30 0 q15 -9 30 0 q15 9 30 0 q15 -9 30 0 q15 9 30 0 q15 -9 30 0 q15 9 30 0 q15 -9 30 0 q15 9 30 0 q15 -9 30 0 q15 9 30 0 q15 -9 30 0 q15 9 30 0 q15 -9 30 0 q15 9 30 0 q15 -9 30 0 q15 9 30 0 q15 -9 30 0 q15 9 30 0 q15 -9 30 0 q15 9 30 0 L1200 34 L0 34 Z" fill="#fff"/>
    <circle cx="632" cy="18" r="14" fill="#101622"/>
  </svg>
</section>

<div class="abs about-img" role="img" aria-label="Person touching a wall of data dashboards"></div>
<div class="abs about-card">
  <h2 class="section-title">ABOUT US</h2>
  <p>Sed ut perspiciatis unde omnis iste natus error sit voluptatem accusantium doloremque laudantium, totam rem aperiam, eaque ipsa quae ab illo inventore veritatis et quasi architecto beatae vitae dicta sunt explicabo.</p>
  <span class="btn">Read More</span>
</div>

<section class="abs dba" role="img" aria-label="Engineer working on a laptop in a dim office">
  <h2 class="abs section-title">REMOTE DBA TEAM OFFERING<br>DATA PLATFORM MANAGEMENT</h2>
  <p class="abs">Sed ut perspiciatis unde omnis iste natus error sit voluptatem accusantium doloremque laudantium, totam rem aperiam, eaque ipsa quae ab illo inventore veritatis et quasi architecto beatae vitae dicta sunt explicabo. Nemo enim ipsam voluptatem quia voluptas sit aspernatur aut odit aut fugit, sed quia consequuntur magni dolores eos qui ratione voluptatem nesciunt.</p>
  <span class="abs btn">Learn More</span>
</section>

<h2 class="abs section-title services-title">OUR SERVICES</h2>
<p class="abs services-text">Sed ut perspiciatis unde omnis iste natus error sit voluptatem<br>accusantium doloremque laudantium</p>
<svg class="abs" style="left:28px;top:2032px" width="50" height="24"><path d="M48 12H6M16 2L4 12l12 10" stroke="#5a2fd6" stroke-width="4" fill="none"/></svg>
<svg class="abs" style="left:1122px;top:2032px" width="50" height="24"><path d="M2 12h42M34 2l12 10-12 10" stroke="#2a6ee0" stroke-width="4" fill="none"/></svg>
<div class="abs card card-photo" style="left:89px" role="img" aria-label="Support team working at laptops with headsets">
  <svg class="abs card-arrow" viewBox="0 0 40 36"><rect width="40" height="36" fill="#222"/><path d="M16 10l8 8-8 8" stroke="#fff" stroke-width="4" fill="none"/></svg>
</div>
<div class="abs card card-feature" style="left:430px">DATA PLATFORM<br>ADMINISTRATION
  <svg class="abs card-arrow" viewBox="0 0 40 36"><rect width="40" height="36" fill="#222"/><path d="M16 10l8 8-8 8" stroke="#fff" stroke-width="4" fill="none"/></svg>
</div>
<div class="abs card card-photo tech" style="left:772px" role="img" aria-label="Engineer holding a tablet in a data center">
  <svg class="abs card-arrow" viewBox="0 0 40 36"><rect width="40" height="36" fill="#222"/><path d="M16 10l8 8-8 8" stroke="#fff" stroke-width="4" fill="none"/></svg>
</div>

<section class="abs testi">
  <h2 class="abs heading">TESTIMONIALS</h2>
  <svg class="abs" style="left:270px;top:112px" width="44" height="34"><text x="0" y="46" font-size="64" font-weight="700" font-family="Georgia,serif" fill="#fff">&#8220;</text></svg>
  <blockquote class="abs">Sed ut perspiciatis unde omnis iste natus error sit voluptatem accusantium doloremque laudantium, totam rem aperiam, eaque ipsa quae ab illo inventore veritatis et quasi architecto beatae vitae dicta sunt explicabo</blockquote>
  <svg class="abs" style="left:888px;top:206px" width="44" height="34"><text x="0" y="46" font-size="64" font-weight="700" font-family="Georgia,serif" fill="#fff">&#8221;</text></svg>
  <div class="abs name">MAREK HOLDEN</div>
  <svg class="abs" style="left:183px;top:332px" width="24" height="36"><path d="M20 2L4 18l16 16" stroke="#fff" stroke-width="4" fill="none"/></svg>
  <svg class="abs" style="left:984px;top:332px" width="24" height="36"><path d="M4 2l16 16L4 34" stroke="#fff" stroke-width="4" fill="none"/></svg>
  <div class="abs avatar" style="left:276px;top:308px;width:82px;height:82px" role="img" aria-label="Client portrait"></div>
  <div class="abs avatar" style="left:404px;top:308px;width:82px;height:82px" role="img" aria-label="Client portrait"></div>
  <div class="abs avatar main" style="left:546px;top:296px;width:106px;height:106px" role="img" aria-label="Portrait of the quoted client"></div>
  <div class="abs avatar" style="left:712px;top:308px;width:82px;height:82px" role="img" aria-label="Client portrait"></div>
  <div class="abs avatar" style="left:842px;top:308px;width:82px;height:82px" role="img" aria-label="Client portrait"></div>
  <div class="abs track"><span></span></div>
</section>

<section class="abs contact" role="img" aria-label="Team collaborating at a desk, tinted blue">
  <h2 class="abs heading">CONTACT US</h2>
  <div class="abs field" style="left:180px;top:161px;width:409px">First Name</div>
  <div class="abs field" style="left:608px;top:161px;width:409px">Last Name</div>
  <div class="abs field" style="left:180px;top:214px;width:409px">Company Name</div>
  <div class="abs field" style="left:180px;top:265px;width:409px">Email Address</div>
  <div class="abs field" style="left:180px;top:317px;width:409px">Phone Number</div>
  <div class="abs field" style="left:608px;top:212px;width:409px;height:144px">Message :</div>
  <span class="abs btn">Submit</span>
</section>

<footer class="abs footer">
  <svg class="abs" style="left:0;top:-18px" width="1200" height="34" viewBox="0 0 1200 34" preserveAspectRatio="none">
    <path d="M0 18 q15 -9 30 0 q15 9 30 0 q15 -9 30 0 q15 9 30 0 q15 -9 30 0 q15 9 30 0 q15 -9 30 0 q15 9 30 0 q15 -9 30 0 q15 9 30 0 q15 -9 30 0 q15 9 30 0 q15 -9 30 0 q15 9 30 0 q15 -9 30 0 q15 9 30 0 q15 -9 30 0 q15 9 30 0 q15 -9 30 0 q15 9 30 0 q15 -9 30 0 q15 9 30 0 q15 -9 30 0 q15 9 30 0 q15 -9 30 0 q15 9 30 0 q15 -9 30 0 q15 9 30 0 q15 -9 30 0 q15 9 30 0 q15 -9 30 0 q15 9 30 0 q15 -9 30 0 q15 9 30 0 q15 -9 30 0 q15 9 30 0 q15 -9 30 0 q15 9 30 0 q15 -9 30 0 q15 9 30 0 L1200 34 L0 34 Z" fill="#f1f1f4"/>
    <circle cx="560" cy="16" r="12" fill="#2160cf"/>
  </svg>
  <div class="abs logo">BRIVOLAN</div>
  <div class="abs tag">Want to make an impact? Provide your email<br>and we'll be in touch.</div>
  <div class="abs subscribe">Enter your email address<span><svg width="44" height="38"><path d="M14 19h16M24 13l6 6-6 6" stroke="#fff" stroke-width="2" fill="none"/></svg></span></div>

  <div class="abs fcol links" style="left:483px;top:78px">
    <h3>QUICK LINKS</h3>
    <ul><li>Home</li><li>About us</li><li>Services</li><li>Blog</li><li>Contact</li></ul>
  </div>
  <div class="abs fcol info" style="left:702px;top:78px">
    <h3>CONTACT US</h3>
    <ul>
      <li><svg width="16" height="18"><path d="M8 1a6 6 0 0 1 6 6c0 5-6 10-6 10S2 12 2 7a6 6 0 0 1 6-6z" fill="#5a2fd6"/><circle cx="8" cy="7" r="2.2" fill="#fff"/></svg>18,40/3 Harlow Street<br>Brenton, Ohio, 44120</li>
      <li><svg width="16" height="16"><path d="M3 1l3 0 2 4-2 2c1 2 3 4 5 5l2-2 4 2v3c-8 1-15-6-14-14z" fill="#5a2fd6"/></svg>Phone: (555) 014 - 2290</li>
      <li><svg width="16" height="14"><rect x="1" y="2" width="14" height="10" fill="#5a2fd6"/><path d="M1 2l7 6 7-6" stroke="#fff" fill="none"/></svg>Email: info@brivolan.cz</li>
    </ul>
  </div>
  <div class="abs fcol social" style="left:974px;top:78px">
    <h3>SOCIAL</h3>
    <ul><li>Netlink</li><li>Pagebook</li><li>Snapgram</li></ul>
  </div>
</footer>

<div class="abs bottom">Copyrights © 2018 All Rights Reserved</div>

</body>
</html>
```